Yoga Magazine needs 6x9 advertising flyer / postcard

I need a flyer (postcard) for my yoga magazine to hand out to businesses. The front side will serve as a WHO WE ARE, THIS IS WHAT WE DO, ETC....the back side will be ADVERTISING INFORMATION including advertising rates.

please see MS Word doc attached to this brief.

Please bleed artwork on to 6.25" x 9.25" (1/8' extra on all sides)

Target Market(s)

WOMEN ages 20-60 who practice yoga.....and some men, but mostly women.

Industry/Entity Type

Advertising

Font styles to use
Serif

Requirements
Must have
• Please find some stock photos of some nice looking, athletic people doing yoga..
Nice to have
• light and bright colors!
Should not have
• no cartoon figures

```html
<!DOCTYPE html>
<html lang="en">
<head>
<meta charset="utf-8">
<title>Lotus Path Magazine – Advertising Flyer</title>
<link rel="stylesheet" href="https://fonts.googleapis.com/css2?family=Cinzel:wght@400;700&family=Arimo:wght@400;700&family=Open+Sans:wght@400;600;700&display=swap">
<style>
:root{
  --stage:#2b2b2b;
  --lime:#d6df2c;
  --orange:#f47a20;
  --orange-light:#f9a24a;
  --orange-deep:#f26a16;
  --ink:#1d1d1d;
  --white:#ffffff;
  --cream:#f6f2e7;
  --rule:#5a5a5a;
  --sand:#e9dcc4;
}
*{box-sizing:border-box;margin:0;padding:0}
html,body{width:1200px;height:944px;overflow:hidden;background:var(--stage)}
.canvas{position:relative;width:1200px;height:944px}
.page{position:absolute;box-shadow:0 4px 14px rgba(0,0,0,.5)}

/* front */
.front{left:40px;top:40px;width:556px;height:838px;background:var(--white);overflow:hidden;font-family:Arimo,Arial,sans-serif}
.front .orange-col{position:absolute;left:278px;top:0;width:278px;height:355px;background:var(--orange)}
.front .lime-head{position:absolute;left:0;top:10px;width:278px;height:105px;background:var(--lime)}
.headline{position:absolute;left:22px;top:24px;font-family:Cinzel,serif;color:var(--ink);line-height:1.08;text-transform:uppercase}
.headline .sm{font-size:19px;letter-spacing:1px}
.headline .lg{font-size:27px;letter-spacing:.5px}
.photo-main{position:absolute;left:302px;top:-5px;width:270px;height:270px;border-radius:50%;border:4px solid var(--white);background:linear-gradient(180deg,#d8e6ee 0%,#eef3f5 55%,#cfc6b8 100%)}
.photo-small{position:absolute;left:278px;top:236px;width:128px;height:128px;border-radius:50%;border:4px solid var(--white);background:linear-gradient(160deg,#e8ecef,#cdd3d6)}
.meaning{position:absolute;left:28px;top:127px;width:242px}
.sec-title{font-family:Cinzel,serif;font-weight:700;font-size:14px;letter-spacing:.5px;color:var(--ink);margin-bottom:5px;text-transform:uppercase}
.meaning p{font-size:11.4px;line-height:14.9px;text-align:justify;color:var(--ink)}
.title-band{position:absolute;left:0;top:355px;width:556px;height:53px;background:var(--lime);text-align:center;font-family:Cinzel,serif;font-weight:700;font-size:34px;line-height:53px;color:var(--ink)}
.lower-left{position:absolute;left:0;top:408px;width:278px;height:430px;background:linear-gradient(180deg,#fff 0%,#fdf4ea 60%,#fbe8d4 100%)}
.lower-right{position:absolute;left:278px;top:408px;width:278px;height:430px;background:linear-gradient(180deg,var(--orange-light) 0%,var(--orange) 45%,var(--orange-deep) 100%)}
.list-block{position:absolute;left:28px;width:240px}
.ticks{list-style:none;font-size:12.2px;line-height:16.3px;color:var(--ink)}
.ticks li::before{content:"\2714";font-size:9px;margin-right:4px}
.info-block{position:absolute;left:297px;width:240px;color:var(--white)}
.info-block .sec-title{color:var(--white);font-weight:400;font-size:15px;margin-bottom:6px}
.info-block p{font-size:11.8px;line-height:14px;text-align:justify}

/* back */
.back{left:619px;top:40px;width:556px;height:836px;background:linear-gradient(180deg,var(--cream) 0%,#f3ede0 60%,var(--sand) 100%);font-family:"Open Sans",Arial,sans-serif;color:var(--ink)}
.back h2{position:absolute;left:0;width:556px;top:32px;text-align:center;font-size:17px;font-weight:700}
.back h2 span{font-weight:400;font-size:15px}
.rates{position:absolute;left:10px;top:68px;width:534px;border-collapse:collapse;background:rgba(255,255,255,.55);font-size:11px}
.rates td,.rates th{border:1px solid var(--rule);height:33px;text-align:center;font-weight:400}
.rates th{height:37px;font-size:12px}
.rates th:first-child{text-align:left;padding-left:8px;font-weight:700;font-size:13px}
.rates td:first-child{text-align:left;padding-left:8px}
.box{position:absolute;left:10px;width:534px;border:1px solid var(--rule);background:rgba(255,255,255,.35)}
.surcharge{top:378px;height:186px;font-size:11px}
.surcharge .row1{padding:10px 8px;border-bottom:1px solid var(--rule);white-space:nowrap}
.surcharge b{font-weight:700;font-size:12px}
.surcharge h4{font-weight:700;font-size:12.5px;margin:10px 10px 4px}
.surcharge ul{margin-left:24px;font-size:11px;line-height:18px}
.specs{top:572px;height:234px;display:flex}
.specs .col-a{width:290px;border-right:1px solid var(--rule);padding:8px 10px;font-size:9.8px;line-height:13.5px}
.specs .col-a h4{font-size:12px;margin-bottom:4px}
.specs .col-a p{margin-bottom:5px}
.specs .col-b{padding:10px 12px;font-size:13.5px;line-height:22px}
.specs .col-b h4{font-size:12px;margin-bottom:6px}
</style>
</head>
<body>
<div class="canvas">
  <section class="page front">
    <div class="orange-col"></div>
    <div class="lime-head"></div>
    <div class="headline"><div class="sm">San Diego's First Free</div><div class="lg">Yoga Magazine</div><div class="sm">Is Here!!!</div></div>
    <div class="photo-main" role="img" aria-label="Woman in a yoga lunge on a sunny beach deck"></div>
    <div class="photo-small" role="img" aria-label="Man in a yoga forward fold pose"></div>
    <div class="meaning">
      <div class="sec-title">The Meaning of Namaste:</div>
      <p>‘Namaste’ or ‘namaskar’ is the Hindu way of greeting and saying goodbye to people. It is not a superficial gesture or a mere word...it is deeper and is for all people - young and old, friends and strangers. You’ll often hear it spoken in combination with a slight bow and the Anjali Mudra – the placement of the hands together pulled close to the heart in a fashion similar to a prayer pose. In Sanskrit, the word ‘namah’ means BOW, ‘as’ means I, and ‘te’ means YOU, translating roughly into "I bow to you," or "I bow to the good (godly) qualities in you."</p>
    </div>
    <div class="title-band">Lotus Path Magazine</div>
    <div class="lower-left" role="img" aria-label="Faint silhouette of a woman doing yoga at sunset"></div>
    <div class="lower-right"></div>
    <div class="list-block" style="top:420px">
      <div class="sec-title">Where We Can Be Found:</div>
      <ul class="ticks">
        <li>Yoga studios</li><li>Gyms / Fitness Facilities</li><li>Health Food Stores</li><li>Restaurants</li><li>Organic Grocery Markets</li><li>Massage Therapists and Acupuncturists</li><li>Chiropractor’s, Doctor’s &amp; Dentist’s offices</li><li>Veterinarians</li><li>Real Estate Office Lobbies</li>
      </ul>
    </div>
    <div class="list-block" style="top:603px">
      <div class="sec-title">Distribution Areas:</div>
      <ul class="ticks">
        <li>Carlsbad</li><li>Encinitas</li><li>Solana Beach</li><li>Del Mar</li><li>Carmel Valley</li><li>UTC</li><li>La Jolla</li><li>Pacific Beach</li><li>Mission Valley (Winter 2015)</li><li>North Park (Winter 2015)</li><li>Hillcrest (Winter 2015)</li><li>Balboa Park (Winter 2015)</li>
      </ul>
    </div>
    <div class="info-block" style="top:420px">
      <div class="sec-title">Who We Are:</div>
      <p>Lotus Path Magazine is San Diego's original yoga magazine! We are a free magazine that is distributed every other month throughout San Diego. We have articles on yoga, health, family, nutrition, pets, fitness, recipes and other inspirational topics. In every issue, we have an "events" section dedicated to upcoming community gatherings, a section for astrology, and also a community</p>
    </div>
    <div class="info-block" style="top:602px">
      <div class="sec-title">Locally Focused:</div>
      <p>Our magazine is published with a local focus, which means that almost all the events and advertisers are from the San Diego area. Our articles are predominantly written by local writers, with the occasional national personality thrown in for fresh perspective. Support LOCAL!</p>
    </div>
    <div class="info-block" style="top:738px">
      <div class="sec-title">Our Promise:</div>
      <p>With our dedication to the community and you, we promise to continually bring top quality, trustworthy and local sources of information to the pages of Lotus Path Magazine.</p>
    </div>
  </section>

  <section class="page back" role="img" aria-label="Faint beach scene with a seated meditating figure in the background">
    <h2>ADVERTISING INFORMATION <span>(All rates listed are per issue)</span></h2>
    <table class="rates">
      <tr><th>All rates listed are per issue.</th><th>One Issue</th><th>Two Issue</th><th>Three Issue</th><th>Four Issue</th></tr>
      <tr><td>Business Card (3.5”w x 2”h)</td><td>$110</td><td>$100</td><td>$90</td><td>$75</td></tr>
      <tr><td>1/4 Page (3.8”w x 5”h)</td><td>$225</td><td>$210</td><td>$195</td><td>$180</td></tr>
      <tr><td>1/2 Page Horizontal (5”w x 7.75”h)</td><td>$450</td><td>$420</td><td>$390</td><td>$360</td></tr>
      <tr><td>1/2 Page Vertical (3.8”w x 10.25”h)</td><td>$450</td><td>$420</td><td>$390</td><td>$360</td></tr>
      <tr><td>Full Page (8.5”w x 11”h)</td><td>$800</td><td>$750</td><td>$725</td><td>$700</td></tr>
      <tr><td>Page 3 (8.5”w x 11”h)</td><td>$1,500</td><td>$1,425</td><td>$1,350</td><td>$1,275</td></tr>
      <tr><td>Inside Cover (8.5”w x 11”h)</td><td>$1,225</td><td>$1,150</td><td>$1,075</td><td>$1,000</td></tr>
      <tr><td>Back Cover (8.5”w x 11”h)</td><td>$2,250</td><td>$2,200</td><td>$2,150</td><td>$2,100</td></tr>
    </table>
    <div class="box surcharge">
      <div class="row1"><b>Color Surcharge:</b>&nbsp; Full Page add $100; Half Page add $85; ¼ page add $65; Business Card add $35</div>
      <h4>Directories: Holistic, Restaurant, Green Business and Yoga Related</h4>
      <ul>
        <li>65 Spaces per line, 1 line, FOUR ISSUES for $80</li>
        <li>65 Spaces per line, 2 lines, FOUR ISSUES for $150</li>
        <li>65 Spaces per line, 3 lines, FOUR ISSUES for $225</li>
      </ul>
      <h4>Event Listings:</h4>
      <ul><li>50 words for $15 (50 word maximum)</li></ul>
    </div>
    <div class="box specs">
      <div class="col-a">
        <h4>Ad Specs:</h4>
        <p>Final trim size: 8.5”x11”.</p>
        <p>Please keep text 0.125” away from edges</p>
        <p>Full-page ad size: 8.25”x10.5” for non-bleeds;<br>8.625”x11.25” for bleeds.</p>
        <p>Please inquire about specs for other print<br>and digital edition positions</p>
        <p>Binding: Saddle stitch</p>
        <p>Stock and inks: Artwork colors should be CMYK;<br>artwork with PMS colors, metallic colors and<br>spot varnish will not be accepted</p>
        <p>Advertiser must provide logo and artwork as<br>press-quality JPG, EPS, TIF or PDF files</p>
      </div>
      <div class="col-b">
        <h4>AD QUESTIONS or ARTWORK:</h4>
        Dev Marlow<br>Lotus Path Magazine<br>Publisher<br>hello@lotuspathmag.com<br>858-555-0142
      </div>
    </div>
  </section>
</div>
</body>
</html>
```